Communications & Broadcast Consulting/PR/Media Relations & Public Affairs

My main goals are to provide communications support to school districts, small towns/cities/hospitals and private businesses in the form of press releases, media relations, public affairs. I also have 25 years experience as a television news anchor/reporter and I'm open to free-lance reporting in both Indianapolis and other markets. My specialty is working with the media.
Communications

```html
<!DOCTYPE html>
<html lang="en">
<head>
<meta charset="utf-8">
<title>Ridgeline Communications – Business Card</title>
<link href="https://fonts.googleapis.com/css2?family=Cinzel:wght@400&family=Quicksand:wght@400;500&family=Tinos&display=swap" rel="stylesheet">
<style>
  :root {
    --page-bg: #2a2a2d;
    --card-mid: #7ab7e6;
    --band-bright: #1d8fe1;
    --band-top: #5aa0e6;
    --band-bottom: #4c84d5;
    --strip-bottom: #3b74cc;
    --art-deep: #3f74c9;
    --art-soft: #8cc2ec;
    --ink-light: #ffffff;
  }
  * { margin: 0; padding: 0; box-sizing: border-box; }
  html, body {
    width: 1200px; height: 800px; overflow: hidden;
    background: var(--page-bg);
  }
  .card {
    position: absolute; left: 75px; top: 100px;
    width: 1050px; height: 600px;
    background: var(--card-mid);
    overflow: hidden;
    color: var(--ink-light);
  }
  .band { position: absolute; }
  .band--top { left: 0; top: 0; width: 100%; height: 24px; background: var(--band-top); }
  .band--company { left: 470px; top: 24px; width: 580px; height: 104px; background: var(--band-bright); }
  .band--name { left: 0; top: 128px; width: 1050px; height: 108px; background: var(--band-bright); opacity: .92; }
  .band--contact { left: 0; top: 440px; width: 100%; height: 125px; background: var(--band-bottom); }
  .band--foot { left: 0; top: 565px; width: 100%; height: 35px; background: var(--strip-bottom); }

  .artwork { position: absolute; left: 0; top: 0; width: 1050px; height: 600px; }

  .company-name {
    position: absolute; left: 540px; top: 42px;
    font-family: "Cinzel", serif; font-weight: 400; line-height: 1.05;
  }
  .company-name__first { display: block; font-size: 34px; letter-spacing: 22px; }
  .company-name__second { display: block; font-size: 34px; letter-spacing: 5px; }

  .person { position: absolute; left: 62px; top: 150px; }
  .person__name { font-family: "Cinzel", serif; font-size: 30px; letter-spacing: 1px; font-weight: 400; }
  .person__role { font-family: "Quicksand", sans-serif; font-size: 18px; line-height: 1.3; margin-top: 4px; padding-left: 14px; }

  .contact { position: absolute; left: 140px; top: 452px; list-style: none; }
  .contact__item {
    display: flex; align-items: center; gap: 20px;
    font-family: "Tinos", serif; font-size: 27px; letter-spacing: 3px;
    height: 38px;
  }
  .contact__icon { width: 30px; height: 30px; flex: none; }

  .address {
    position: absolute; right: 60px; top: 318px;
    font-family: "Tinos", serif; font-size: 26px; letter-spacing: 2px;
    line-height: 1.22; text-align: right; font-style: normal;
  }
  .address__pin { position: absolute; left: -50px; top: 2px; width: 28px; height: 36px; }
</style>
</head>
<body>
  <main class="card">
    <div class="band band--top"></div>
    <div class="band band--name"></div>
    <div class="band band--company"></div>
    <div class="band band--contact"></div>
    <div class="band band--foot"></div>

    <svg class="artwork" viewBox="0 0 1050 600" role="img" aria-label="Illustration of a broadcast transmission tower rising over a city skyline">
      <defs>
        <linearGradient id="tower-fade" x1="0" y1="0" x2="0" y2="1">
          <stop offset="0" stop-color="var(--art-soft)" stop-opacity="0"/>
          <stop offset="1" stop-color="var(--art-deep)" stop-opacity=".55"/>
        </linearGradient>
        <linearGradient id="skyline-fade" x1="0" y1="0" x2="0" y2="1">
          <stop offset="0" stop-color="var(--art-deep)" stop-opacity="0"/>
          <stop offset="1" stop-color="var(--art-deep)" stop-opacity=".5"/>
        </linearGradient>
      </defs>
      <rect x="400" y="130" width="330" height="435" fill="url(#tower-fade)"/>
      <rect x="0" y="380" width="1050" height="185" fill="url(#skyline-fade)"/>
    </svg>

    <h1 class="company-name">
      <span class="company-name__first">RIDGELINE</span>
      <span class="company-name__second">COMMUNICATIONS</span>
    </h1>

    <section class="person">
      <h2 class="person__name">DANA WHITFIELD</h2>
      <p class="person__role">Public &amp; Media Relations<br>Consultant</p>
    </section>

    <ul class="contact">
      <li class="contact__item">
        <svg class="contact__icon" viewBox="0 0 30 30" aria-hidden="true">
          <path d="M3 11c0-4 5-6 12-6s12 2 12 6v2h-6v-3H9v3H3z" fill="#fff"/>
          <path d="M7 15h16l3 11H4z" fill="#fff"/>
          <circle cx="15" cy="20" r="3" fill="var(--band-bottom)"/>
        </svg>
        <span>555.201.4410</span>
      </li>
      <li class="contact__item">
        <svg class="contact__icon" viewBox="0 0 30 30" aria-hidden="true">
          <rect x="8" y="2" width="14" height="26" rx="3" fill="none" stroke="#fff" stroke-width="2.5"/>
          <circle cx="15" cy="24" r="1.5" fill="#fff"/>
        </svg>
        <span>555.201.7723</span>
      </li>
      <li class="contact__item">
        <svg class="contact__icon" viewBox="0 0 30 30" aria-hidden="true">
          <rect x="2" y="7" width="26" height="17" fill="#fff"/>
          <path d="M2 7l13 10 13-10" fill="none" stroke="var(--band-bottom)" stroke-width="2"/>
        </svg>
        <span>dwhitfield@ridgelinemail.com</span>
      </li>
    </ul>

    <address class="address">
      <svg class="address__pin" viewBox="0 0 28 36" aria-hidden="true">
        <path d="M14 1C7 1 2 6 2 13c0 9 12 22 12 22s12-13 12-22C26 6 21 1 14 1z" fill="#fff"/>
        <circle cx="14" cy="13" r="4.5" fill="var(--card-mid)"/>
      </svg>
      Ridgeline<br>
      Communications<br>
      2718 Larkspur Lane<br>
      Fairview, IN 46000
    </address>
  </main>
</body>
</html>
```